Business Card Design and Stationary design for consulting firm

Harbourline Sourcing are looking for a new business card design and a design for their A4 letterhead / A4 invoices.

We are seeking to heavily increase our brand awareness and require a business card that's professional in appearance but also shows flare and innovation. A card design that people will remember.

About Us
Harbourline Sourcing are `The Sourcing Crew’.
Our mission is to be one of Australia’s greatest companies. Our aim is to help our customers achieve the best result from their purchasing experience.

Our Requirement:
• IMPACT! IMPACT! IMPACT!
• BUSINESS & PROFESSIONAL LOOKING

• Our business colours are orange, blue and green (See the logo attached).

We have provided an Art Design specification (attached) that needs to be followed for you to win the design. This also has the font, which is used on the logo.

We are after a two sided business card

Side One should have the:
The company Logo
The Sourcing Crew
www.harbourlinesourcing.com.au
Source | Staffing | Supply & Compliance
Northport | Eastvale | Southbay | Westmere

Side Two
Logo (optional)
Harbourline Sourcing (optional)
Employee details (details listed below)

The above format is our preferred option, but if you think you can come up with something better, feel free to put it forward.

We are leaving the design up to you, but it must incorporate the logo.

We will need a template that we can change the employee details on, as we will be adding more staff over the coming months.

The details below are for one employee per card with the same design.
------------------------

Employee Details:

Marcus Del Arroyo MBA, MMgmtStratProc
Principal Consultant
0491 372 618
Marcus@harbourlinesourcing.com.au

Brianna Tolley
Consulting Manager
0462 915 308
Brianna@harbourlinesourcing.com.au

Our website is www.harbourlinesourcing.com.au

The Letterhead / invoice needs to incorporate:
the company Logo
The Sourcing Crew
Northport | Eastvale | Southbay | Westmere but otherwise the design is over to you.

This file needs to be delivered in word format as other detail will be added to the documents.

We look forward to you award winning designs. If you require any further information please feel free to contact us.

Regards
Harbourline Sourcing

Target Market(s)

Our Target market is companies with 80+ employees. The market we segment is heavily male based, between the ages of 35-55 years of age.

Industry/Entity Type

Consulting

Contact Information for Business Card

See Project Description

Font styles to use
Other font styles liked:
• See Art Specification

Requirements
Must have
• Company Colours, See Project Description
Should not have
• Be outside the Art specification guidelines

```html
<!DOCTYPE html>
<html lang="en">
<head>
<meta charset="utf-8">
<title>Harbourline Sourcing – Business Card</title>
<link rel="stylesheet" href="https://fonts.googleapis.com/css2?family=Open+Sans:wght@400;600&display=swap">
<style>
  :root {
    --page-bg: #e9e6e1;
    --card-bg: #ffffff;
    --ink: #2b2b2b;
    --ink-soft: #3a3a3a;
    --band-dark: #1d1d1d;
    --band-text: #e6e6e6;
    --accent-orange: #f18a1f;
    --side-grey: #9a9a9a;
    --brand-grey: #4a4a4a;
  }
  * { margin: 0; padding: 0; box-sizing: border-box; }
  html, body {
    width: 1200px; height: 838px; overflow: hidden;
    background: var(--page-bg);
    font-family: "Open Sans", Arial, sans-serif;
  }
  .card {
    position: absolute; left: 100px; top: 113px;
    width: 1000px; height: 611px;
    background: var(--card-bg);
    overflow: hidden;
  }
  .side-strip {
    position: absolute; right: 0; top: 0;
    width: 56px; height: 100%;
    background: var(--side-grey);
  }
  .side-strip-notch { position: absolute; left: 0; top: 204px; }
  .brand {
    position: absolute; left: 48px; top: 44px; width: 336px;
    text-align: center; color: var(--brand-grey); font-weight: 600;
  }
  .brand-dot {
    width: 124px; height: 124px; border-radius: 50%;
    background: var(--accent-orange);
    margin: 0 auto 26px;
  }
  .brand-name { font-size: 42px; letter-spacing: 3px; line-height: 1.1; }
  .brand-sub { font-size: 22px; letter-spacing: 6px; line-height: 1.3; }
  .person {
    position: absolute; right: 87px; top: 186px; text-align: right;
  }
  .person-name { font-size: 40px; font-weight: 600; color: var(--ink); line-height: 1.3; }
  .person-title { font-size: 28px; color: var(--ink-soft); letter-spacing: 1px; line-height: 1.5; }
  .contact-band { position: absolute; left: 0; top: 367px; }
  .contact-lines {
    position: absolute; right: 91px; top: 377px;
    text-align: right; color: var(--band-text);
    font-size: 27px; letter-spacing: 1.5px; line-height: 36px;
  }
  .accent-rule {
    position: absolute; left: 0; top: 497px;
    width: 944px; height: 10px; background: var(--accent-orange);
  }
  .services {
    position: absolute; left: 42px; top: 518px;
    font-size: 28px; color: var(--ink); letter-spacing: 1.5px; line-height: 37px;
  }
</style>
</head>
<body>
  <main class="card">
    <div class="side-strip">
      <svg class="side-strip-notch" width="26" height="50" viewBox="0 0 26 50">
        <polygon points="0,0 24,25 0,50" fill="var(--card-bg)"/>
      </svg>
    </div>

    <div class="brand">
      <div class="brand-dot"></div>
      <div class="brand-name">HARBOURLINE</div>
      <div class="brand-sub">SOURCING</div>
    </div>

    <div class="person">
      <div class="person-name">Brianna Tolley</div>
      <div class="person-title">Consulting Manager</div>
    </div>

    <svg class="contact-band" width="944" height="134" viewBox="0 0 944 134">
      <polygon points="300,0 944,0 944,134 229,134" fill="var(--band-dark)"/>
    </svg>
    <div class="contact-lines">
      <div>0462 915 308</div>
      <div>www.harbourlinesourcing.com.au</div>
      <div>Brianna@harbourlinesourcing.com.au</div>
    </div>

    <div class="accent-rule"></div>

    <div class="services">
      <div>Source | Staffing | Supply &amp; Compliance</div>
      <div>Northport | Eastvale | Southbay | Westmere</div>
    </div>
  </main>
</body>
</html>
```